Post Card (5x7) - Pre-foreclosure Image - Harbor Path Partners

(Two-Sided Post Card)
FACING FORECLOSURE? YOU STILL HAVE OPTIONS.
If you’re behind on payments or at risk of foreclosure, you’re not alone—and it’s not too late to take action.
We help homeowners:
• Explore options to stay in their home
• Stop or delay foreclosure
• Sell quickly for a fair price if needed
No pressure. No obligation. Just real solutions tailored to your situation.
Call - (240) 558-2094
Email - marcus@hpbllc-mail.com
Harbor Path Partners LLC
7200 Bramwick Lane, Ellicott City, MD 21043
**Marcus Fennimore is a Licensed Realtor with Copperleaf Homes Realty in Bethesda, Maryland.
(Leave room for mailing address, return address & postage)
Target Market(s)
Distressed Homeowners
Industry/Entity Type
Real Estate

```html
<!DOCTYPE html>
<html lang="en">
<head>
<meta charset="utf-8">
<title>Harbor Path Partners – Pre-foreclosure Postcard</title>
<link href="https://fonts.googleapis.com/css2?family=Outfit:wght@300;400;500;700;800&family=Roboto:wght@400&display=swap" rel="stylesheet">
<style>
  :root {
    --page: #9b9b9b;
    --crimson: #9e2d48;
    --ember: #e8561e;
    --sun: #f7b733;
    --ink: #050505;
    --panel: #111111;
    --white: #ffffff;
    --gold: #f5c928;
    --rule: #c9c9c9;
    --stamp: #8a8a8a;
  }
  * { box-sizing: border-box; margin: 0; padding: 0; }
  html, body { width: 833px; height: 1200px; overflow: hidden; }
  body { background: var(--page); position: relative; font-family: "Outfit", sans-serif; color: var(--white); }

  .card { position: absolute; overflow: hidden; }

  /* ---------- Front ---------- */
  .front { left: 64px; top: 56px; width: 703px; height: 510px; background: var(--ink); }
  .front__sky {
    position: absolute; left: 0; top: 0; width: 703px; height: 420px;
    background: linear-gradient(180deg, var(--crimson) 0%, #a8344a 28%, #d9472d 46%, var(--ember) 58%, var(--sun) 70%, #e3641c 80%, var(--ink) 100%);
  }
  .front__frame { position: absolute; left: 17px; top: 19px; width: 670px; height: 330px; border: 1px solid var(--white); border-bottom: none; }
  .front__frame-gap { position: absolute; left: 287px; top: -2px; width: 92px; height: 4px; background: var(--crimson); }

  .brand { position: absolute; left: 0; width: 100%; text-align: center; }
  .brand__mark { display: block; margin: 0 auto 8px; width: 30px; height: 30px; border: 2px solid var(--white); }
  .brand__name { font-weight: 500; letter-spacing: 0.16em; text-transform: uppercase; color: var(--white); line-height: 1.25; }
  .front .brand { top: 26px; }
  .front .brand__name { font-size: 20px; }

  .headline { position: absolute; left: 0; width: 100%; text-align: center; font-weight: 800; line-height: 1; letter-spacing: -0.01em; }
  .headline__lead { display: block; font-size: 30px; margin-top: 0; }
  .headline__main { display: block; font-size: 40px; margin-top: 4px; }
  .front .headline { top: 142px; }
  .front__intro { position: absolute; left: 80px; width: 543px; top: 222px; text-align: center; font-size: 16.5px; font-weight: 400; line-height: 1.22; }

  .services { position: absolute; left: 0; top: 428px; width: 703px; height: 60px; }
  .services__label { position: absolute; left: 38px; top: 6px; font-size: 12px; font-weight: 500; color: var(--gold); line-height: 1.2; }
  .services__label::after { content: ""; display: block; width: 18px; height: 1px; background: var(--white); margin-top: 6px; }
  .service { position: absolute; top: 0; display: flex; align-items: center; gap: 8px; }
  .service__icon { width: 45px; height: 45px; flex: none; }
  .service__text { font-size: 11.5px; font-weight: 300; line-height: 1.2; }
  .promise { position: absolute; left: 535px; top: 2px; color: var(--gold); }
  .promise__ticks { font-size: 8.5px; font-weight: 400; display: flex; gap: 8px; }
  .promise__ticks span { display: inline-flex; align-items: center; gap: 2px; }
  .promise__line { font-size: 12px; font-weight: 500; line-height: 1.25; margin-top: 4px; }

  /* ---------- Back ---------- */
  .back { left: 62px; top: 615px; width: 708px; height: 513px; background: var(--white); }
  .back__photo {
    position: absolute; left: 0; top: 0; width: 385px; height: 241px;
    background: linear-gradient(180deg, #4e5560 0%, #7d7566 35%, #c98a3a 55%, #3a2f24 72%, #1c1a18 100%);
  }
  .back .brand { top: 138px; width: 385px; }
  .back .brand__mark { width: 24px; height: 24px; margin-bottom: 8px; }
  .back .brand__name { font-size: 16px; }
  .back__panel { position: absolute; left: 0; top: 243px; width: 385px; height: 270px; background: var(--panel); }
  .agent__portrait {
    position: absolute; left: 38px; top: 29px; width: 94px; height: 94px; border-radius: 50%;
    border: 2px solid var(--white); background: radial-gradient(circle at 50% 40%, #6d7a55 0%, #3d4a33 60%, #2a2a2a 100%);
  }
  .agent__name { position: absolute; left: 143px; top: 46px; font-size: 24px; font-weight: 700; }
  .agent__license { position: absolute; left: 143px; top: 78px; font-family: "Roboto", sans-serif; font-size: 10.5px; line-height: 1.3; width: 200px; }
  .back__rule { position: absolute; left: 36px; top: 140px; width: 327px; height: 1px; background: #3a3a3a; }
  .contact { position: absolute; left: 36px; display: flex; align-items: center; gap: 8px; font-size: 14px; font-weight: 300; }
  .contact svg { flex: none; }
  .contact--phone { top: 157px; }
  .contact--email { top: 175px; }
  .contact--office { top: 204px; align-items: center; gap: 9px; line-height: 1.25; }

  .mailing__stamp { position: absolute; left: 595px; top: 18px; width: 95px; height: 103px; border: 1px solid var(--stamp); }
  .mailing__line { position: absolute; left: 425px; width: 265px; height: 1px; background: var(--rule); }
</style>
</head>
<body>

<section class="card front" aria-label="Postcard front">
  <div class="front__sky" role="img" aria-label="City skyline silhouetted against a crimson and orange sunset"></div>
  <div class="front__frame"><div class="front__frame-gap"></div></div>

  <div class="brand">
    <span class="brand__mark"></span>
    <div class="brand__name">Harbor Path<br>Partners LLC</div>
  </div>

  <h1 class="headline">
    <span class="headline__lead">FACING FORECLOSURE?</span>
    <span class="headline__main">YOU STILL HAVE OPTIONS.</span>
  </h1>
  <p class="front__intro">If you’re behind on payments or at risk of foreclosure, you’re not alone—and it’s not too late to take action.</p>

  <div class="services">
    <div class="services__label">We help<br>homeowners</div>

    <div class="service" style="left:124px">
      <svg class="service__icon" viewBox="0 0 45 45" fill="none" stroke="#fff" stroke-width="1.2">
        <polygon points="13,1.5 32,1.5 43.5,13 43.5,32 32,43.5 13,43.5 1.5,32 1.5,13"/>
        <path d="M12 22 L22 13 L32 22 M15 20 V31 H24"/>
        <circle cx="28" cy="28" r="4"/><path d="M31 31 L34 34"/>
      </svg>
      <div class="service__text">Explore options<br>to stay in their<br>home</div>
    </div>

    <div class="service" style="left:268px">
      <svg class="service__icon" viewBox="0 0 45 45" fill="none" stroke="#fff" stroke-width="1.2">
        <polygon points="13,1.5 32,1.5 43.5,13 43.5,32 32,43.5 13,43.5 1.5,32 1.5,13"/>
        <path d="M12 20 L21 12 L30 20 M14 18 V32 H22"/>
        <rect x="23" y="22" width="10" height="12"/><path d="M25 26 H31 M25 29 H31"/>
      </svg>
      <div class="service__text">Stop or<br>delay<br>foreclosure</div>
    </div>

    <div class="service" style="left:391px">
      <svg class="service__icon" viewBox="0 0 45 45" fill="none" stroke="#fff" stroke-width="1.2">
        <polygon points="13,1.5 32,1.5 43.5,13 43.5,32 32,43.5 13,43.5 1.5,32 1.5,13"/>
        <path d="M11 20 L22.5 11 L34 20 M14 18 V32 H31 V18"/>
        <rect x="16" y="21" width="13" height="7"/><path d="M22.5 28 V34"/>
      </svg>
      <div class="service__text">Sell quickly<br>for a fair price<br>if needed</div>
    </div>

    <div class="promise">
      <div class="promise__ticks">
        <span><svg width="9" height="9" viewBox="0 0 9 9" fill="none" stroke="#fff" stroke-width="1"><rect x="0.5" y="0.5" width="8" height="8" rx="1.5"/><path d="M2 4.5 L4 6.5 L8 1.5"/></svg>No pressure.</span>
        <span><svg width="9" height="9" viewBox="0 0 9 9" fill="none" stroke="#fff" stroke-width="1"><rect x="0.5" y="0.5" width="8" height="8" rx="1.5"/><path d="M2 4.5 L4 6.5 L8 1.5"/></svg>No obligation.</span>
      </div>
      <div class="promise__line">Just real solutions tailored<br>to your situation.</div>
    </div>
  </div>
</section>

<section class="card back" aria-label="Postcard back">
  <div class="back__photo" role="img" aria-label="City skyline across a river at sunset"></div>
  <div class="brand">
    <span class="brand__mark"></span>
    <div class="brand__name">Harbor Path<br>Partners LLC</div>
  </div>

  <div class="back__panel">
    <div class="agent__portrait" role="img" aria-label="Portrait of Marcus Fennimore"></div>
    <div class="agent__name">Marcus Fennimore</div>
    <p class="agent__license">is a Licensed Realtor with Copperleaf Homes Realty in Bethesda, Maryland.</p>
    <div class="back__rule"></div>

    <div class="contact contact--phone">
      <svg width="14" height="14" viewBox="0 0 24 24" fill="none" stroke="#fff" stroke-width="1.5"><path d="M5 3h4l2 5-2.5 1.5a11 11 0 0 0 6 6L16 13l5 2v4a2 2 0 0 1-2 2A17 17 0 0 1 3 5a2 2 0 0 1 2-2z"/></svg>
      <span>(240) 558-2094</span>
    </div>
    <div class="contact contact--email">
      <svg width="14" height="12" viewBox="0 0 24 18" fill="none" stroke="#fff" stroke-width="1.5"><rect x="1" y="1" width="22" height="16"/><path d="M1 1 L12 10 L23 1"/></svg>
      <span>marcus@hpbllc-mail.com</span>
    </div>
    <div class="contact contact--office">
      <svg width="26" height="28" viewBox="0 0 26 28" fill="none" stroke="#fff" stroke-width="1.5"><path d="M13 22 C7 15 5 12 5 9 a8 8 0 0 1 16 0 c0 3-2 6-8 13z"/><circle cx="13" cy="9" r="3"/><path d="M8 20 L2 26 H24 L18 20"/></svg>
      <span>Harbor Path Partners LLC<br>7200 Bramwick Lane, Ellicott City, MD 21043</span>
    </div>
  </div>

  <div class="mailing__stamp"></div>
  <div class="mailing__line" style="top:201px"></div>
  <div class="mailing__line" style="top:261px"></div>
  <div class="mailing__line" style="top:322px"></div>
  <div class="mailing__line" style="top:382px"></div>
</section>

</body>
</html>
```